Plaxo - Booking activities for Kids and Adults.

The app allows booking of Kid's activities for a given date/time.
The app lists activities offered via various clubs (vendors) which a user can book for their kids.
The users can browse various clubs and their offered activities. The users can manage their kid's profiles.
Need a whole new look to the app. The existing app can be checked out at
https://store.example-apps.test/details?id=com.plaxokw
https://apps.example-store.test/us/app/plaxo-بلاكسو/id9072514863?ls=1
Try using the app as Guest.

Target Market(s)

Kuwait

Font styles to use
Serif
Sans Serif

Requirements
Must have
• Home Screens
The home page should have everything from the existing app and a quick area to change between different kid's profile to see activities matching their interests ONLY. In the current version, there's no switch profile and hence we are showing the name tags on the activities.

We are also going to build ecommerce so we need that ecommerce look and feel.
Kindly maintain the image aspect ratio from the current app so the new version doesn't require new images.

Need a complete new innovative designs - Keep the color scheme same.
The designs should be minimalistic and image oriented. The design should be done in XD. The designs should be submitted in both light and dark theme.
Reference to be used - http://brindle.example.uk

D.M for more info if needed.

```html
<!DOCTYPE html>
<html lang="en">
<head>
<meta charset="utf-8">
<title>Select Interests</title>
<link rel="stylesheet" href="https://fonts.googleapis.com/css2?family=Poppins:wght@300;400;500;600;700;800&display=swap">
<style>
  :root {
    --page-bg: #f8f8f8;
    --surface: #ffffff;
    --ink: #2f2f2f;
    --ink-soft: #6b6b6b;
    --ink-muted: #a8a8a8;
    --divider: #d6d6d6;
    --orange: #f7941d;
    --orange-dark: #d97c10;
    --teal: #43c4c0;
    --teal-dark: #2ea7a3;
    --dance-chip: #fbf1d5;
    --dance-icon: #f2b632;
    --sports-chip: #e3f4f3;
    --sports-icon: #3fb8b4;
    --edu-chip: #f0e4ec;
    --edu-icon: #9b4a86;
    --card-sports: #fbebe3;
    --card-sports-title: #f7a233;
    --card-dance: #ffcad8;
    --card-dance-title: #f65f8e;
    --card-edu: #9ee0dd;
    --card-edu-title: #10aab4;
    --card-art: #f9ede0;
    --card-art-title: #f58634;
  }
  * { box-sizing: border-box; margin: 0; padding: 0; }
  html, body { width: 1200px; height: 2592px; overflow: hidden; }
  body {
    position: relative;
    background: var(--page-bg);
    font-family: "Poppins", sans-serif;
    color: var(--ink);
  }

  .app-header {
    position: absolute; left: 0; top: 0; width: 1200px; height: 359px;
    background: var(--surface);
    border-radius: 0 0 100px 100px;
    box-shadow: 0 10px 40px rgba(0,0,0,0.06);
  }
  .status-time {
    position: absolute; left: 97px; top: 30px;
    font-size: 47px; font-weight: 500; letter-spacing: -1px; color: #111;
  }
  .status-icons { position: absolute; right: 66px; top: 44px; }
  .back-button { position: absolute; left: 64px; top: 214px; }
  .screen-title {
    position: absolute; left: 0; width: 1200px; top: 190px; text-align: center;
    font-size: 57px; font-weight: 700; letter-spacing: 1px; color: var(--ink);
  }

  .profile-photo {
    position: absolute; left: 70px; top: 465px; width: 198px; height: 213px;
    border: 6px solid var(--surface); border-radius: 20px;
    background: linear-gradient(160deg, #7fcbe6, #56b3d6 60%, #c9a48a);
    box-shadow: 0 4px 14px rgba(0,0,0,0.08);
  }
  .profile-name {
    position: absolute; left: 309px; top: 444px;
    font-size: 78px; font-weight: 700; letter-spacing: 2px; color: var(--ink);
  }
  .profile-note {
    position: absolute; left: 312px; top: 560px; width: 820px;
    font-size: 35px; font-weight: 400; line-height: 54px; color: var(--ink-soft);
  }

  .category-chip {
    position: absolute; top: 745px; width: 160px; text-align: center;
  }
  .chip-circle {
    width: 160px; height: 160px; border-radius: 50%;
    display: flex; align-items: center; justify-content: center;
  }
  .chip-label {
    position: absolute; top: 163px; left: -60px; width: 280px;
    font-size: 33px; font-weight: 500; color: var(--ink);
  }
  .chip-all { left: 72px; }
  .chip-all .chip-circle { background: var(--orange); }
  .chip-dance { left: 286px; }
  .chip-dance .chip-circle { background: var(--dance-chip); }
  .chip-sports { left: 500px; }
  .chip-sports .chip-circle { background: var(--sports-chip); }
  .chip-education { left: 713px; }
  .chip-education .chip-circle { background: var(--edu-chip); }
  .chip-more { left: 969px; }
  .chip-more .chip-circle { border: 3px dashed #333; }

  .section-divider {
    position: absolute; left: 67px; top: 1015px; width: 1065px; height: 2px; background: var(--divider);
  }
  .section-count {
    position: absolute; left: 67px; top: 1093px;
    font-size: 57px; font-weight: 700; letter-spacing: 1px; color: var(--ink);
  }
  .view-all {
    position: absolute; right: 68px; top: 1098px;
    font-size: 40px; font-weight: 700; color: var(--ink-muted);
    text-decoration: underline; text-underline-offset: 10px; text-decoration-thickness: 3px;
  }

  .interest-card {
    position: absolute; border-radius: 30px; overflow: hidden;
  }
  .card-title {
    position: absolute; left: 57px; top: 26px;
    font-size: 50px; font-weight: 700; letter-spacing: 1px;
  }
  .card-select {
    position: absolute; top: 54px; right: 50px; width: 38px; height: 38px;
    border-radius: 50%; border: 5px solid var(--surface);
  }
  .card-select.is-selected { background: var(--surface); border: none; display: flex; align-items: center; justify-content: center; }
  .card-art { position: absolute; left: 50px; right: 50px; border-radius: 24px; }

  .card-sports { left: 67px; top: 1210px; width: 509px; height: 424px; background: var(--card-sports); }
  .card-sports .card-title { color: var(--card-sports-title); }
  .card-sports .card-art { top: 150px; height: 240px; background: linear-gradient(180deg, #f6dccb, #f3c9a9 60%, #8cc86a); }

  .card-dance { left: 618px; top: 1210px; width: 511px; height: 608px; background: var(--card-dance); }
  .card-dance .card-title { color: var(--card-dance-title); }
  .card-dance .card-art { top: 270px; height: 300px; background: linear-gradient(180deg, #ffd9e3, #f9e07a 50%, #f27aa2); }

  .card-education { left: 67px; top: 1667px; width: 509px; height: 610px; background: var(--card-edu); }
  .card-education .card-title { color: var(--card-edu-title); }
  .card-education .card-art { top: 210px; height: 350px; background: linear-gradient(180deg, #bdeae7, #f6b08a 55%, #6fc9c4); }

  .card-crafts { left: 618px; top: 1850px; width: 511px; height: 427px; background: var(--card-art); }
  .card-crafts .card-title { color: var(--card-art-title); }
  .card-crafts .card-art { top: 160px; height: 230px; background: linear-gradient(90deg, #f3d2c0, #f4e7dc 50%, #c9a98c); }

  .action-button {
    position: absolute; top: 2362px; height: 117px; width: 510px;
    border-radius: 60px; color: var(--surface);
    font-size: 47px; font-weight: 700; letter-spacing: 2px;
    display: flex; align-items: center; justify-content: center;
  }
  .button-next { left: 67px; background: var(--orange); box-shadow: 0 6px 0 var(--orange-dark); }
  .button-skip { left: 618px; background: var(--teal); box-shadow: 0 6px 0 var(--teal-dark); }
</style>
</head>
<body>

<header class="app-header">
  <div class="status-time">11:04</div>
  <svg class="status-icons" width="170" height="36" viewBox="0 0 170 36" aria-hidden="true">
    <rect x="0" y="22" width="7" height="10" rx="1.5" fill="#111"/>
    <rect x="11" y="16" width="7" height="16" rx="1.5" fill="#111"/>
    <rect x="22" y="9" width="7" height="23" rx="1.5" fill="#111"/>
    <rect x="33" y="2" width="7" height="30" rx="1.5" fill="#bbb"/>
    <path d="M58 12 a26 26 0 0 1 36 0" stroke="#111" stroke-width="5" fill="none" stroke-linecap="round"/>
    <path d="M64 19 a17 17 0 0 1 24 0" stroke="#111" stroke-width="5" fill="none" stroke-linecap="round"/>
    <circle cx="76" cy="28" r="4.5" fill="#111"/>
    <rect x="110" y="5" width="50" height="26" rx="7" stroke="#111" stroke-width="3" fill="none"/>
    <rect x="114" y="9" width="42" height="18" rx="4" fill="#111"/>
    <rect x="162" y="13" width="4" height="10" rx="2" fill="#111"/>
  </svg>
  <svg class="back-button" width="46" height="40" viewBox="0 0 46 40" aria-label="Back">
    <path d="M44 20 H4 M20 4 L4 20 L20 36" stroke="#222" stroke-width="3.5" fill="none" stroke-linecap="round" stroke-linejoin="round"/>
  </svg>
  <h1 class="screen-title">Select Interests</h1>
</header>

<section class="profile">
  <div class="profile-photo" role="img" aria-label="Profile photo of Tariq"></div>
  <h2 class="profile-name">For Tariq</h2>
  <p class="profile-note">This helps us suggests events and activities that we think your family will enjoy</p>
</section>

<nav class="category-filter">
  <div class="category-chip chip-all">
    <div class="chip-circle">
      <svg width="78" height="78" viewBox="0 0 78 78" aria-hidden="true">
        <rect x="4" y="4" width="50" height="50" rx="10" fill="none" stroke="#fff" stroke-width="5"/>
        <rect x="20" y="20" width="52" height="52" rx="10" fill="#fff"/>
        <path d="M32 46 L42 56 L60 36" stroke="var(--orange)" stroke-width="6" fill="none" stroke-linecap="round" stroke-linejoin="round"/>
      </svg>
    </div>
    <div class="chip-label">All</div>
  </div>
  <div class="category-chip chip-dance">
    <div class="chip-circle">
      <svg width="80" height="80" viewBox="0 0 80 80" role="img" aria-label="Dance icon">
        <path d="M10 72 Q40 20 70 72 Z" fill="var(--dance-icon)"/>
        <circle cx="48" cy="14" r="8" fill="var(--dance-icon)"/>
      </svg>
    </div>
    <div class="chip-label">Dance</div>
  </div>
  <div class="category-chip chip-sports">
    <div class="chip-circle">
      <svg width="84" height="84" viewBox="0 0 84 84" role="img" aria-label="Sports balls icon">
        <circle cx="34" cy="34" r="26" fill="var(--sports-icon)"/>
        <ellipse cx="56" cy="58" rx="22" ry="16" fill="var(--sports-icon)" opacity="0.8"/>
      </svg>
    </div>
    <div class="chip-label">Sports</div>
  </div>
  <div class="category-chip chip-education">
    <div class="chip-circle">
      <svg width="74" height="80" viewBox="0 0 74 80" role="img" aria-label="Education reading icon">
        <circle cx="37" cy="16" r="12" fill="var(--edu-icon)"/>
        <path d="M4 36 L37 46 L70 36 V74 L37 80 L4 74 Z" fill="var(--edu-icon)"/>
      </svg>
    </div>
    <div class="chip-label">Education</div>
  </div>
  <div class="category-chip chip-more">
    <div class="chip-circle">
      <svg width="84" height="20" viewBox="0 0 84 20" aria-label="More categories">
        <circle cx="12" cy="10" r="9" fill="#333"/>
        <circle cx="42" cy="10" r="9" fill="#333"/>
        <circle cx="72" cy="10" r="9" fill="#333"/>
      </svg>
    </div>
  </div>
</nav>

<div class="section-divider"></div>
<h3 class="section-count">35 activities</h3>
<div class="view-all">View All</div>

<article class="interest-card card-sports">
  <div class="card-title">Sports</div>
  <div class="card-select is-selected">
    <svg width="22" height="18" viewBox="0 0 22 18" aria-label="Selected">
      <path d="M2 9 L8 15 L20 3" stroke="#222" stroke-width="3" fill="none" stroke-linecap="round" stroke-linejoin="round"/>
    </svg>
  </div>
  <div class="card-art" role="img" aria-label="Illustration of two people jogging in a park"></div>
</article>

<article class="interest-card card-dance">
  <div class="card-title">Dance</div>
  <div class="card-select"></div>
  <div class="card-art" role="img" aria-label="Illustration of four children dancing"></div>
</article>

<article class="interest-card card-education">
  <div class="card-title">Education</div>
  <div class="card-select"></div>
  <div class="card-art" role="img" aria-label="Illustration of a student at a laptop surrounded by learning icons"></div>
</article>

<article class="interest-card card-crafts">
  <div class="card-title">Art &amp; Crafts</div>
  <div class="card-select"></div>
  <div class="card-art" role="img" aria-label="Illustration of two artists drawing at easels"></div>
</article>

<div class="action-button button-next">NEXT</div>
<div class="action-button button-skip">SKIP</div>

</body>
</html>
```